Business Card Design with existing logo

TealHeron provides inspirational leadership training and coaching for corporate executives. We focus on being challenging, humorous and compassionate, providing the right mix of support and push for individuals and teams to improve their knowledge and performance. The colour purple is essential to the design. We already have a logo we are very happy with - we are curious to see what can be done to come across in a professional, high standard way that sets us apart. Ideally the design should include the photo of Lise-Britt
Target Market(s)
HR/ Senior Management 500 - 1500 employees
Industry/Entity Type
Leadership
Contact Information for Business Card
TealHeron Coaching Ltd
Inspirational leadership
Lise-Britt Holmgaard Pennick
Leadership coach and trainer
Telephone: +44 1632 960 418
Mobile: +44 7700 900 562
e-mail: lisebritt@tealheroncoaching.example
www.tealheroncoaching.example
Requirements
Must have
- The existing logo
Picture of Lise-Britt

```html
<!DOCTYPE html>
<html lang="en">
<head>
<meta charset="utf-8">
<title>TealHeron Coaching – Business Card</title>
<link href="https://fonts.googleapis.com/css2?family=Open+Sans:wght@300;400;600&display=swap" rel="stylesheet">
<style>
  :root {
    --purple: #7044a0;
    --black: #1d1b1e;
    --white: #ffffff;
    --ink: #2a2a2a;
    --stage: #e4e4e6;
  }
  * { box-sizing: border-box; margin: 0; padding: 0; }
  html, body {
    width: 1200px; height: 1200px; overflow: hidden;
    background: var(--stage);
    font-family: "Open Sans", Arial, sans-serif;
  }
  .card {
    position: absolute; top: 445px;
    width: 540px; height: 310px;
    box-shadow: 0 4px 14px rgba(0,0,0,.25);
    overflow: hidden;
  }
  /* Contact side */
  .card--contact { left: 50px; background: var(--white); }
  .side-band { position: absolute; left: 0; top: 0; width: 63px; height: 100%; background: var(--black); }
  .side-line { position: absolute; left: 69px; top: 0; width: 4px; height: 100%; background: var(--black); }
  .brand {
    position: absolute; left: 34px; top: 48px;
    display: flex; align-items: center; gap: 10px;
  }
  .brand__dot { width: 58px; height: 58px; border-radius: 50%; background: var(--purple); flex: none; }
  .brand__name { font-weight: 600; font-size: 22px; color: var(--purple); letter-spacing: .5px; white-space: nowrap; }
  .tagline {
    position: absolute; left: 130px; top: 96px;
    font-size: 7px; letter-spacing: 2.5px; color: var(--ink); text-transform: uppercase;
  }
  .person { position: absolute; left: 84px; top: 138px; width: 440px; }
  .person__name { font-size: 18px; font-weight: 400; color: var(--ink); }
  .person__role {
    font-size: 13px; color: var(--purple); font-weight: 300;
    border-bottom: 1.5px solid var(--purple); padding-bottom: 1px; margin-top: 2px;
  }
  .person__company, .person__motto { font-size: 13px; color: var(--ink); line-height: 1.2; }
  .contacts { position: absolute; left: 84px; top: 223px; font-size: 14px; line-height: 1.1; color: var(--ink); }
  .contacts .accent { color: var(--purple); }
  .icons { position: absolute; left: 48px; top: 226px; display: flex; flex-direction: column; gap: 8px; }
  .icons svg { display: block; }
  .icon-box { width: 9px; height: 9px; background: var(--purple); border-radius: 2px; }

  /* Brand side */
  .card--brand { left: 610px; background: var(--black); }
  .brand-disc { position: absolute; left: 2px; top: 0; width: 292px; height: 292px; border-radius: 50%; background: var(--purple); }
  .brand-wordmark {
    position: absolute; left: 198px; top: 210px;
    font-weight: 600; font-size: 22px; color: var(--white); letter-spacing: 1px;
  }
  .brand-tagline {
    position: absolute; left: 285px; top: 243px;
    font-size: 7px; letter-spacing: 2.5px; color: #cfcfcf; text-transform: uppercase;
  }
</style>
</head>
<body>
  <section class="card card--contact">
    <div class="side-band"></div>
    <div class="side-line"></div>
    <div class="brand">
      <span class="brand__dot"></span>
      <span class="brand__name">TealHeron Coaching</span>
    </div>
    <div class="tagline">Inspirational Leadership</div>
    <div class="person">
      <p class="person__name">Lise-Britt Holmgaard Pennick</p>
      <p class="person__role">Leadership coach and trainer</p>
      <p class="person__company">TealHeron Coaching Ltd</p>
      <p class="person__motto">Inspirational leadership</p>
    </div>
    <div class="icons">
      <svg width="10" height="10" viewBox="0 0 24 24" aria-label="phone"><path fill="#7044a0" d="M6.6 10.8a15 15 0 0 0 6.6 6.6l2.2-2.2a1 1 0 0 1 1-.25 11.4 11.4 0 0 0 3.6.57 1 1 0 0 1 1 1V20a1 1 0 0 1-1 1A17 17 0 0 1 3 4a1 1 0 0 1 1-1h3.5a1 1 0 0 1 1 1c0 1.25.2 2.45.57 3.57a1 1 0 0 1-.25 1z"/></svg>
      <span class="icon-box"></span>
      <span class="icon-box"></span>
    </div>
    <div class="contacts">
      <p>+44 1632 960 418</p>
      <p>+44 7700 900 562 (Mobile)</p>
      <p>lisebritt@tealheroncoaching.example</p>
      <p>www.<span class="accent">tealheroncoaching</span>.example</p>
    </div>
  </section>

  <section class="card card--brand">
    <div class="brand-disc"></div>
    <div class="brand-wordmark">TealHeron Coaching</div>
    <div class="brand-tagline">Inspirational Leadership</div>
  </section>
</body>
</html>
```